Website for IT consulting Company

I need a website upgrade, the existing site content is ok, I would also like to add a testimonial page, the site should be something that is easy for us to update content. You use the content from www.velmarketa.com as an example. I will also post update logo and artwork. I also need a contact form with some type of validation or captcha.

Please omit Address maps

Target Market(s)

small business, service oriented companies. We provide IT Consulting, support and mangement

Industry/Entity Type

Information Technology

Coding

Coded - Design and coding required

Number of Pages Required

1 page

Font styles to use
Serif
Sans Serif

Requirements
Must have
• Contain logo attached, and content from existing web site www.velmarketa.com.
• Also need to update content easily, and be movable to different platforms.
• There is a catch phrase
• "Let us worry about your technology…” “ so you don’t have to!”
• Should be included.
Nice to have
• Testimonial page, Project page where we can post new and past projects and pictures
Should not have
• none

```html
<!DOCTYPE html>
<html lang="en">
<head>
<meta charset="utf-8">
<title>Velmarketa Development Group – IT Support Solutions</title>
<link rel="stylesheet" href="https://fonts.googleapis.com/css2?family=Roboto:ital,wght@0,400;0,500;0,700;1,400&display=swap">
<style>
:root{
  --blue:#3a96e0;
  --blue-deep:#2a7dcf;
  --blue-dark:#1f6fbf;
  --hero-a:#5fb3e6;
  --hero-b:#2f7fc4;
  --ink:#222;
  --muted:#555;
  --paper:#f4f5f7;
  --white:#fff;
  --rule:#9aa7b5;
}
*{box-sizing:border-box;margin:0;padding:0}
html,body{width:694px;height:1200px;overflow:hidden}
body{position:relative;font-family:'Roboto',Arial,sans-serif;color:var(--ink);background:var(--paper)}
.abs{position:absolute}

/* header + hero */
.hero{left:0;top:0;width:694px;height:314px;background:linear-gradient(160deg,var(--hero-a) 0%,#4a9fd8 45%,var(--hero-b) 100%)}
.header{left:0;top:0;width:694px;height:38px;border-bottom:1px solid rgba(255,255,255,.35)}
.brand{left:28px;top:10px;display:flex;align-items:center;gap:5px;color:var(--white);font-weight:700;font-size:15px;letter-spacing:.5px}
.brand-mark{width:13px;height:13px;background:#f28b1f}
.nav{left:216px;top:14px;display:flex;gap:22px;font-size:8.5px;color:var(--white);letter-spacing:.2px}
.phone{left:542px;top:14px;font-size:8px;color:var(--white)}
.btn-contact{left:615px;top:9px;width:52px;height:19px;border-radius:10px;background:var(--white);font-size:7.5px;text-align:center;line-height:19px;color:var(--ink)}
.tagline{left:0;top:136px;width:694px;text-align:center;color:var(--white);font-weight:700;font-size:13px;line-height:23px}
.btn-learn{left:312px;top:185px;width:66px;height:19px;border-radius:3px;background:var(--white);font-size:7.5px;font-weight:700;text-align:center;line-height:19px}

/* welcome */
.welcome{left:0;top:314px;width:694px;height:76px;background:var(--blue);color:var(--white);text-align:center}
.welcome h1{font-size:12.5px;font-weight:700;margin-top:5px}
.welcome hr{border:0;border-top:1px dashed rgba(255,255,255,.8);margin:8px 30px 5px}
.welcome p{font-size:6.8px;line-height:10.5px;padding:0 30px}

/* section titles */
.sec-title{left:0;width:694px;text-align:center;font-size:12.5px;font-weight:700}
.sec-title span{color:var(--blue-deep)}
.dash{left:30px;width:634px;border-top:1px dashed var(--rule)}

/* service cards */
.card{width:200px;height:90px}
.card-photo{position:absolute;left:0;top:0;width:200px;height:88px}
.card-label{position:absolute;left:8px;top:76px;width:184px;height:25px;background:var(--blue);border-radius:2px;color:var(--white);font-size:7.5px;font-weight:500;text-align:center;line-height:25px}
.card-icon{position:absolute;left:87px;top:-14px;width:27px;height:27px;border-radius:50%;background:var(--blue-deep);border:2px solid var(--white)}
.p1{background:linear-gradient(120deg,#3b4556,#8a94a3 60%,#c9ced6)}
.p2{background:linear-gradient(120deg,#2b5fb8,#3f7fd8 55%,#2a4f98)}
.p3{background:linear-gradient(120deg,#e8eaee,#7b8493 50%,#cfd4da)}
.p4{background:linear-gradient(120deg,#5b6470,#9aa2ab 50%,#d8dce0)}
.p5{background:linear-gradient(120deg,#cfc9c0,#8f8a84 50%,#e4e2df)}
.p6{background:linear-gradient(120deg,#f3f4f6,#c9cdd3 50%,#2f3e5c)}

/* feature band */
.feature{top:729px;height:136px;width:232px;color:var(--white);text-align:center;padding:0 28px}
.feature h2{font-size:15.5px;font-weight:700;line-height:15px;margin-top:17px}
.feature p{font-size:8.6px;line-height:13px;margin-top:11px}
.f-a{left:0;background:var(--blue)}
.f-b{left:232px;width:230px;background:var(--blue-deep)}
.f-c{left:462px;background:var(--blue)}

/* testimonials */
.quote{width:236px;font-size:7px;line-height:11.2px;font-style:italic;color:var(--muted)}
.quote b{display:block;font-style:normal;font-weight:400;color:var(--ink);font-size:7px;margin-top:6px}
.q-left{text-align:right}
.avatar{width:44px;height:44px;border-radius:50%;background:radial-gradient(circle at 50% 40%,#d9d6d2,#8f8983)}
.vline{left:347px;border-left:1px dashed var(--rule)}

/* like bar */
.like-line{left:38px;top:1088px;width:618px;border-top:1px solid #dde1e6}
.like-box{left:217px;top:1075px;width:260px;height:27px;border:1px solid #dde1e6;border-radius:14px;background:var(--white)}
.like-thumb{position:absolute;left:0;top:0;width:34px;height:25px;border-right:1px solid #dde1e6}
.like-btn{position:absolute;left:70px;top:8px;width:26px;height:10px;background:#4a6ab3;border-radius:2px;color:var(--white);font-size:5.5px;font-weight:700;text-align:center;line-height:10px}
.like-text{position:absolute;left:100px;top:8px;font-size:5.5px;line-height:10px;color:#333}

/* footer */
.footer{left:0;top:1109px;width:694px;height:91px;background:var(--white);border-top:3px solid var(--blue-deep);border-bottom:3px solid var(--blue-deep)}
.foot-nav{left:36px;top:32px;display:flex;gap:13px;font-size:7.5px;font-weight:700;align-items:center}
.foot-rule{left:36px;top:48px;width:622px;border-top:1px dashed var(--rule)}
.foot-links{left:36px;top:57px;display:flex;gap:13px;font-size:6.5px;color:#333}
.social{left:329px;top:56px;display:flex;gap:4px}
.social i{display:block;width:9px;height:9px;background:var(--blue-deep);border-radius:1px}
.foot-brand{left:558px;top:18px;display:flex;align-items:center;gap:4px;color:var(--blue-deep);font-weight:700;font-size:12.5px;letter-spacing:.4px}
.foot-brand-mark{width:11px;height:11px;background:var(--blue-deep)}
.foot-legal{left:557px;top:57px;display:flex;gap:14px;font-size:6.5px;color:#333}
</style>
</head>
<body>

<div class="abs hero" role="img" aria-label="Blurred office photo of people working at laptops, tinted blue"></div>

<header class="abs header">
  <div class="abs brand"><span class="brand-mark"></span>VELMARKETA</div>
  <nav class="abs nav"><span>ABOUT US</span><span>SUPPORT</span><span>CLIENTS</span><span>PROJECT</span><span>CAREERS</span></nav>
  <div class="abs phone">+1 (555) 014-2290</div>
  <div class="abs btn-contact">Contact Us</div>
</header>

<div class="abs tagline">Let us worry about your technology…<br>so you don’t have to</div>
<div class="abs btn-learn">Learn More</div>

<section class="abs welcome">
  <h1>Welcome to Velmarketa Development Group, Inc</h1>
  <hr>
  <p>VDG is a technology solution provider based in Port Arden, Texas. Our goal is to make technology a non-issue for individuals and small to medium size businesses ranging from 5 to 150 Users.<br>
  VDG has the experience, the tools, high-level technology solutions and training to power your business and your work force. We understand that all business's have one goal in common!<br>
  (VDG) A Return on Investment</p>
</section>

<div class="abs sec-title" style="top:396px">IT Support <span>Solutions</span></div>
<div class="abs dash" style="top:418px"></div>

<div class="abs card" style="left:30px;top:454px"><div class="card-photo p1" role="img" aria-label="Technicians working at a server rack"></div><span class="card-icon"></span><div class="card-label">Network Administration</div></div>
<div class="abs card" style="left:247px;top:454px"><div class="card-photo p2" role="img" aria-label="Bundles of blue network cables"></div><span class="card-icon"></span><div class="card-label">Network Cabling</div></div>
<div class="abs card" style="left:461px;top:454px"><div class="card-photo p3" role="img" aria-label="Business team in discussion"></div><span class="card-icon"></span><div class="card-label">Network Security</div></div>
<div class="abs card" style="left:30px;top:611px"><div class="card-photo p4" role="img" aria-label="Colleagues reviewing a laptop"></div><span class="card-icon"></span><div class="card-label">Desktop Support</div></div>
<div class="abs card" style="left:247px;top:611px"><div class="card-photo p5" role="img" aria-label="Hands using a tablet beside a laptop"></div><span class="card-icon"></span><div class="card-label">Wireless Networks</div></div>
<div class="abs card" style="left:461px;top:611px"><div class="card-photo p6" role="img" aria-label="Professional working at a computer"></div><span class="card-icon"></span><div class="card-label">Antivirus Solutions</div></div>

<div class="abs feature f-a"><h2>IT Infrastructure Design and Installation</h2><p>Our staff will design, service, administer and maintain your IT needs.<br>We are well versed on all major operating system, and network appliances</p></div>
<div class="abs feature f-b"><h2>Managed IT Solutions</h2><p>Do you need a quick solution to a technical problem? With our live remote-assistance tool, a member of our support team can view your desktop and share control of your mouse and keyboard to get you on your way to a solution.</p></div>
<div class="abs feature f-c"><h2>Remote Diagnostic and Support</h2><p>Do you have more than one site? Do you need remote access? We can design and implement LANS/WANS and VPN's. Make your important data available to you wherever you are.</p></div>

<div class="abs sec-title" style="top:873px">What <span>People Say</span></div>
<div class="abs dash" style="top:895px"></div>
<div class="abs vline" style="top:922px;height:126px"></div>
<div class="abs dash" style="top:985px"></div>

<div class="abs quote q-left" style="left:32px;top:922px">Duis aute irure dolor in reprehenderit in voluptate velit esse cillum dolore eu fugiat nulla pariatur. Excepteur sint occaecat cupidatat non proident, sunt in culpa qui officia deserunt mollit.<b>Reid Calloway, Operations Manager</b></div>
<div class="abs avatar" style="left:284px;top:922px" role="img" aria-label="Portrait of a client"></div>
<div class="abs avatar" style="left:366px;top:922px" role="img" aria-label="Portrait of a client"></div>
<div class="abs quote" style="left:427px;top:922px">Provident, similique sunt in culpa qui officia deserunt mollitia animi, id est laborum et dolorum fuga. Et harum quidem rerum facilis est et expedita distinctio. Nam libero tempore, cum soluta nobis.<b>Nora Pell, Creative Designer</b></div>

<div class="abs quote q-left" style="left:32px;top:1002px">Luis aute irure dolor in reprehenderit in piluptate velit esse cillum dolore eu fugiat nulla pariatur. Excepteur sint occaecat cupidatat non proident, sunt in culpa qui officia deserunt mollit.<b>Ines Marlow, Manager</b></div>
<div class="abs avatar" style="left:284px;top:1002px" role="img" aria-label="Portrait of a client"></div>
<div class="abs avatar" style="left:366px;top:1002px" role="img" aria-label="Portrait of a client"></div>
<div class="abs quote" style="left:427px;top:1002px">At vero eos et accusamus et iusto odio dignissimos ducimus qui blanditiis praesentium voluptatum deleniti atque corrupti quos dolores et quas molestias excepturi sint occaecati asperiores.<b>Owen Tarrant, Developer</b></div>

<div class="abs like-line"></div>
<div class="abs like-box">
  <span class="like-thumb"></span>
  <span class="like-btn">Like</span>
  <span class="like-text">You and 4k others like this.</span>
</div>

<footer class="abs footer">
  <nav class="abs foot-nav">
    <svg width="8" height="8" viewBox="0 0 8 8" aria-hidden="true"><circle cx="3.2" cy="3.2" r="2.4" fill="none" stroke="#444" stroke-width="1.1"/><line x1="5" y1="5" x2="7.5" y2="7.5" stroke="#444" stroke-width="1.2"/></svg>
    <span>Help &amp; Contact</span><span>Support</span><span>Project</span><span>Clients</span>
  </nav>
  <div class="abs foot-brand"><span class="foot-brand-mark"></span>VELMARKETA</div>
  <div class="abs foot-rule"></div>
  <div class="abs foot-links"><span>About</span><span>Blog</span><span>Careers</span><span>Public Policy</span><span>Sitemap</span><span>Partners</span></div>
  <div class="abs social"><i></i><i></i><i></i></div>
  <div class="abs foot-legal"><span>© 2007–2017</span><span>Privacy</span><span>Legal</span></div>
</footer>

</body>
</html>
```